Business Card For Quillmoor Financial Consulting

Hi, I would like a business card designed. Bold, modern.
Please use the same design as the logo. I have also attached the website design to see the overall theme.
Wordmark Font
Color: Hex: #01AEF7

```html
<!DOCTYPE html>
<html lang="en">
<head>
<meta charset="utf-8">
<title>Quillmoor Financial Consulting — Business Card</title>
<link href="https://fonts.googleapis.com/css2?family=Lato:wght@400;700&family=Montserrat:wght@600;700&display=swap" rel="stylesheet">
<style>
  :root {
    --backdrop: #6e6e6e;
    --card: #18222d;
    --card-deep: #121a23;
    --accent: #01aef7;
    --ink: #ffffff;
    --muted: #8a96a3;
  }
  * { box-sizing: border-box; margin: 0; padding: 0; }
  html, body { width: 1200px; height: 800px; overflow: hidden; }
  body {
    background: var(--backdrop);
    font-family: "Lato", sans-serif;
    color: var(--ink);
    position: relative;
  }
  .card {
    position: absolute;
    top: 230px;
    width: 540px;
    height: 320px;
    background: var(--card);
    border-bottom: 6px solid var(--accent);
    box-shadow: 0 14px 30px rgba(0,0,0,0.35);
    overflow: hidden;
  }
  .card--front { left: 50px; }
  .card--back { left: 610px; }

  /* Front */
  .brand-chip {
    position: absolute;
    top: 26px;
    right: 28px;
    display: flex;
    align-items: center;
    gap: 8px;
    font-family: "Lato", sans-serif;
    font-weight: 700;
    font-size: 15px;
    color: var(--accent);
    letter-spacing: 0.5px;
  }
  .brand-chip__square {
    width: 18px; height: 18px;
    border: 2px solid var(--accent);
  }
  .identity {
    position: absolute;
    left: 60px;
    top: 160px;
    text-align: right;
    width: 200px;
  }
  .identity__name {
    font-family: "Montserrat", sans-serif;
    font-weight: 700;
    font-size: 24px;
    letter-spacing: 1px;
    line-height: 1.1;
  }
  .identity__role {
    font-size: 17px;
    color: var(--accent);
    margin-top: 2px;
  }
  .divider {
    position: absolute;
    left: 280px;
    top: 120px;
    width: 1px;
    height: 120px;
    background: var(--muted);
  }
  .contacts {
    position: absolute;
    left: 300px;
    top: 122px;
    list-style: none;
    font-size: 13px;
    line-height: 1.45;
  }
  .contacts li { display: flex; align-items: flex-start; gap: 9px; }
  .contacts svg { width: 12px; height: 12px; margin-top: 3px; flex: none; }
  .contacts__gap { margin-left: 21px; }

  /* Back */
  .pattern-field {
    position: absolute;
    inset: 0;
    background: linear-gradient(110deg, #3d5f80 0%, #22374c 28%, #18222d 55%, #10171f 100%);
  }
  .wordmark {
    position: absolute;
    left: 50%;
    top: 50%;
    transform: translate(-50%, -50%);
    display: flex;
    align-items: center;
    gap: 14px;
    background: var(--card);
    padding: 14px 20px;
  }
  .wordmark__square {
    width: 30px; height: 30px;
    border: 3px solid var(--accent);
    flex: none;
  }
  .wordmark__name {
    font-family: "Lato", sans-serif;
    font-weight: 700;
    font-size: 22px;
    color: var(--ink);
    letter-spacing: 1px;
    white-space: nowrap;
  }
</style>
</head>
<body>

<section class="card card--front">
  <div class="brand-chip"><span class="brand-chip__square"></span>Quillmoor</div>

  <div class="identity">
    <p class="identity__name">ELIAS MARLOW</p>
    <p class="identity__role">Founder &amp; CEO</p>
  </div>

  <div class="divider"></div>

  <ul class="contacts">
    <li>
      <svg viewBox="0 0 12 12"><path d="M6 0.5a4 4 0 0 1 4 4c0 3-4 7-4 7s-4-4-4-7a4 4 0 0 1 4-4z" fill="var(--accent)"/><circle cx="6" cy="4.5" r="1.4" fill="var(--card)"/></svg>
      <span>Your Address<br>City, State, Zip 1235</span>
    </li>
    <li>
      <svg viewBox="0 0 12 12"><path d="M2.5 1l2 2-1 1.5a7 7 0 0 0 4 4l1.5-1 2 2-1.5 1.5C5 10.5 1.5 7 1 2.5z" fill="var(--accent)"/></svg>
      <span>(123) 456-7890</span>
    </li>
    <li>
      <svg viewBox="0 0 12 12"><rect x="3" y="0.5" width="6" height="11" rx="1" fill="none" stroke="var(--accent)" stroke-width="1.3"/><circle cx="6" cy="9.5" r="0.7" fill="var(--accent)"/></svg>
      <span>(231) 456-7890</span>
    </li>
    <li>
      <svg viewBox="0 0 12 12"><rect x="0.5" y="2" width="11" height="8" fill="var(--accent)"/><path d="M0.5 2l5.5 4.5L11.5 2" fill="none" stroke="var(--card)" stroke-width="1"/></svg>
      <span>info@quillmoorconsulting.com</span>
    </li>
    <li>
      <svg viewBox="0 0 12 12"><circle cx="6" cy="6" r="5.2" fill="none" stroke="var(--accent)" stroke-width="1.3"/><path d="M1 6h10M6 1c-2 3-2 7 0 10M6 1c2 3 2 7 0 10" fill="none" stroke="var(--accent)" stroke-width="0.9"/></svg>
      <span>quillmoorconsulting.com</span>
    </li>
  </ul>
</section>

<section class="card card--back">
  <div class="pattern-field" role="img" aria-label="Repeating embossed brand-mark pattern, fading from light steel blue on the left to near black on the right"></div>
  <div class="wordmark">
    <span class="wordmark__square"></span>
    <span class="wordmark__name">Quillmoor Financial Consulting</span>
  </div>
</section>

</body>
</html>
```